Postcard to Market Greeting Cards

Need a Postcard to
* Promote a particular human being and his story.
* Market and raise awareness of his art
* Advertise his website where the art can be purchased.

Background:
Davor Kelmandi is a refugee and artist trapped in a refugee camp in Indonesia.
He has committed no crimes. He had to escape his country as a refugee.
He is currently held in detention. The only way out is to be privately sponsored.
This costs a huge amount of money. Davor is working to raise the money needed.
He is young and has lost 5 years being imprisoned. We must work to save him.

He draws everyday and sends the drawings to me. I make them into beautiful hand drawn art cards which we sell at markets, on the internet or via contacts.
He is not allowed to work. Secret drawing is the only way he can make a living.

This postcard is to
* share some of Davor's Story and to give a sense of who he is.
* display his beautiful art cards which are sold for income via his website.
* Prominently display his website address as well as images of the cards.

These postcards will be given out at markets, letterbox dropped, sent to new customers, left in cafes and libraries etc so people will discover Davor's Cards....
By buying the cards...Davor can earn the funds he needs to pay for sponsorship into a free country. Many countries will accept him if he pays for the process.

Therefore...the postcard needs to be filled front and back. No need to leave space for address and postage. This leaves more room for samples of the Greeting Cards.

There is text provided for the front and back of the POSTCARD.
This may be edited and added to as the design process continues.

Images of Davor's Cards have been uploaded for you.
It would be great if these can be beautifully and artistically presented on the postcard. The aim is to attract people to Davor's hand drawn cards motivate people to want to buy them. Not all of the card images need to be used.

There are * black line cards * colour cards. * framed colour art works
so some of each could be promoted on the postcard.

Davor's Story will be included on the back of the card labelled for the Back.
A few words will be clearly and displayed on the front. Labelled fo the front.

The front art can be a single drawing image from Davor OR a collage of many OR
It can contain his image or a few small images. See what you feel works well as there is scope to create a BEAUTIFUL postcard that depicts beautiful CARDS.

There is a quote from Davor to be included on the front.
Can it be written in a handwriting style font to make it look like Davor has written the message himself ?

There are images of Davor to be used on the front and back.
Davor's images have ben taken on dodgy phones and may not be a good quality.
They don't need to be large images and they DON'T need to all be used. There is a selection to choose from.

Davor is in a prison. Maybe there are design elements that might remind of this.
Barbed wire maybe. Fences. The over all feel though is FREEDOM and BEAUTY in the hand drawn art cards and the escape they will provide in the end.

Davor's website to be displayed on the front and back
davorsketch.net

email address on the back
helpdavor2031@mailpost.net

These postcards will encourage buyers to read Davor's Story and want to help.
They will display beautifully hand drawn art cards which people will want to buy.
They will display the website address prominently and in some clever. arty way.

Good luck with it all.
I plan to increase first prize money depending on the designs....
and to offer more than first place depending on the deigns.

Please feel free to ask me any questions at any time.

Good luck and thanks for considering this project.

Neil Farrow

Target Market(s)

Broad human rights supporters who will enjoy seeing a human story and will want to. respond.

Industry/Entity Type

Human Rights

Colors

Designer to choose colors to be used in the design.

Requirements
Must have
• Colourful and imaginative way of displaying the Greeting Cards being marketed by the Postcard. It is a taster and a sampling. They do not need to be arranged in rows or order..better to be creative in displaying the samples of cards. The website has the organised online shop. The postcard is a sampler and should MAKE people want to go to the website to buy the cards. The postcard must share the story of the artist.
• Handwriting font for the quote from the artist to make it look like he has written a personal message.
• Postcard needs to be filled on front and back. No blank space for mailing and address.
Nice to have
• Free and easy arty design. Photograph of the artist placed in some creative way.
Should not have
• Conservative structure. Free and arty is better.
• The postcard needs to be filled on the front and back ! No need to leave the bank area for mailing as it will only be used for marketing and distribution. it won't actually be used for mailing.

```html
<!DOCTYPE html>
<html lang="en">
<head>
<meta charset="utf-8">
<title>Free Davor – Postcard</title>
<link rel="stylesheet" href="https://fonts.googleapis.com/css2?family=Roboto+Condensed:wght@700&family=Arimo:wght@400;700&family=Playfair+Display:wght@400&family=Kaushan+Script&family=Nothing+You+Could+Do&family=Vazirmatn:wght@400;600&display=swap">
<style>
  :root {
    --page: #e9eaec;
    --wood-dark: #4f3b2d;
    --wood-mid: #6b5443;
    --wood-light: #7d6552;
    --seam: rgba(30, 20, 12, 0.45);
    --green: #1d4d2c;
    --green-deep: #163d22;
    --white: #ffffff;
    --cream: #f4e7c4;
    --orange: #e2562a;
    --farsi-green: #2f9a6a;
    --ink: #1b1b1b;
    --shadow: 0 6px 14px rgba(0, 0, 0, 0.45);
  }
  * { box-sizing: border-box; margin: 0; padding: 0; }
  html, body { width: 820px; height: 1200px; overflow: hidden; }
  body { background: var(--page); position: relative; font-family: "Arimo", Arial, sans-serif; }

  .postcard {
    position: absolute; left: 85px; width: 650px; height: 502px;
    box-shadow: 0 8px 18px rgba(0, 0, 0, 0.35);
  }
  .postcard--front { top: 75px; }
  .postcard--back { top: 616px; }

  .wood {
    position: absolute; inset: 0;
    background:
      repeating-linear-gradient(180deg, transparent 0 44px, var(--seam) 44px 46px),
      repeating-linear-gradient(90deg, transparent 0 210px, rgba(30,20,12,0.25) 210px 212px),
      radial-gradient(ellipse at 55% 45%, var(--wood-light), var(--wood-mid) 55%, var(--wood-dark));
  }

  .band {
    position: absolute; left: 0; background: var(--green);
    box-shadow: 0 4px 10px rgba(0, 0, 0, 0.4);
  }
  .postcard--front .band { top: 114px; width: 657px; height: 115px; }
  .postcard--back .band { top: 364px; width: 650px; height: 116px; }

  .headline {
    position: absolute; right: 36px; top: 28px;
    font-family: "Roboto Condensed", "Arial Narrow", sans-serif; font-weight: 700;
    font-size: 64px; line-height: 1; color: var(--white); letter-spacing: 0.5px;
  }
  .band-pitch {
    position: absolute; left: 337px; width: 300px; top: 124px;
    color: var(--white); text-align: center; font-size: 16.5px; line-height: 24px;
  }
  .band-pitch strong { font-weight: 700; }

  .quote {
    position: absolute; left: 340px; top: 256px; width: 300px;
    font-family: "Nothing You Could Do", cursive; color: var(--white);
    font-size: 14px; line-height: 19.5px;
  }
  .quote-mark { font-family: Georgia, serif; font-size: 30px; line-height: 0; vertical-align: -8px; margin-right: 4px; }

  .call-out {
    position: absolute; left: 366px; width: 260px; top: 388px;
    text-align: center; color: var(--white); font-weight: 700; font-size: 12px; line-height: 16.5px;
  }

  .url-ribbon { position: absolute; }
  .url-ribbon svg { position: absolute; inset: 0; }
  .url-ribbon span {
    position: relative; display: block; text-align: center; color: var(--green-deep);
    font-size: 21px; letter-spacing: 0.3px;
  }
  .url-ribbon b { font-weight: 700; }
  .postcard--front .url-ribbon { left: 367px; top: 449px; width: 248px; height: 31px; }
  .postcard--front .url-ribbon span { line-height: 31px; }
  .postcard--back .url-ribbon { left: 189px; top: 438px; width: 260px; height: 34px; }
  .postcard--back .url-ribbon span { line-height: 34px; font-size: 22px; }

  .art-card {
    position: absolute; background: var(--white); box-shadow: var(--shadow);
    padding: 8px; display: flex; flex-direction: column; align-items: center;
  }
  .card-title {
    font-family: "Playfair Display", Georgia, serif; color: var(--orange);
    font-size: 15px; line-height: 1; letter-spacing: 0.3px; margin-top: 6px;
  }
  .card-farsi {
    font-family: "Vazirmatn", Tahoma, sans-serif; color: var(--farsi-green);
    font-size: 10px; line-height: 14px; margin-bottom: 4px;
  }
  .card-art { width: 100%; flex: 1; }
  .card-art--blush { background: linear-gradient(160deg, #e7c9bf, #c99384); }
  .card-art--gold { background: linear-gradient(160deg, #f0d59b, #d6a95e); }
  .card-art--ivory { background: linear-gradient(160deg, #f6ecd6, #e9d2a8); }
  .card-art--pencil { background: linear-gradient(160deg, #d4d4d4, #9c9c9c); flex: none; }
  .card-art--rose { background: linear-gradient(160deg, #f1d6d3, #d8a9a0); }
  .card-word {
    font-family: "Kaushan Script", cursive; color: var(--ink); font-size: 25px; line-height: 1.1; margin-top: 3px;
  }
  .card-word-farsi { font-family: "Vazirmatn", Tahoma, sans-serif; color: var(--ink); font-size: 12px; line-height: 15px; }

  .card-peace { left: 6px; top: 72px; width: 154px; height: 206px; transform: rotate(-2.5deg); }
  .card-love { left: 173px; top: 74px; width: 158px; height: 198px; transform: rotate(2deg); }
  .card-be { left: 6px; top: 312px; width: 110px; height: 150px; transform: rotate(-2deg); padding: 7px; }
  .card-joy { left: 114px; top: 306px; width: 105px; height: 144px; padding: 6px; }
  .card-still { left: 220px; top: 312px; width: 110px; height: 150px; transform: rotate(2.5deg); padding: 7px; }
  .card-be .card-art--pencil, .card-still .card-art--pencil { height: 78px; }
  .card-joy .card-title { font-size: 12px; margin-top: 3px; }

  .card-hope { left: 64px; top: 20px; width: 101px; height: 168px; transform: rotate(-1.5deg); }
  .card-gentle { left: 181px; top: 20px; width: 134px; height: 168px; }
  .card-gentle .card-art--pencil { height: 96px; }
  .card-compassion { left: 330px; top: 20px; width: 137px; height: 168px; }
  .card-compassion .card-title { font-size: 13px; }
  .card-framed { left: 480px; top: 20px; width: 134px; height: 172px; transform: rotate(4deg); padding: 9px; }

  .story {
    position: absolute; left: 17px; top: 202px; width: 617px;
    color: var(--white); font-weight: 700; font-size: 11px; line-height: 13.4px; text-align: justify;
  }
  .story p + p { margin-top: 5px; }

  .portrait {
    position: absolute; left: 17px; top: 354px; width: 154px; height: 126px;
    background: var(--white); padding: 7px; box-shadow: var(--shadow); transform: rotate(-3deg);
  }
  .portrait-photo { width: 100%; height: 100%; background: linear-gradient(160deg, #b9a58a, #6e6150 60%, #d8d6d2); }

  .offer {
    position: absolute; left: 187px; top: 384px; color: var(--white); font-size: 11.5px; line-height: 15px;
  }
  .email {
    position: absolute; left: 462px; top: 448px; color: var(--white); font-size: 11px;
    display: flex; align-items: center; gap: 5px;
  }
</style>
</head>
<body>

<section class="postcard postcard--front" aria-label="Postcard front">
  <div class="wood" role="img" aria-label="Weathered brown wooden planks"></div>
  <div class="band"></div>

  <article class="art-card card-peace">
    <h3 class="card-title">BE PEACE</h3>
    <p class="card-farsi" lang="fa">صلح باش</p>
    <div class="card-art card-art--blush" role="img" aria-label="Painting of orange trumpet flowers on a soft pink ground"></div>
  </article>
  <article class="art-card card-love">
    <h3 class="card-title">BE LOVE</h3>
    <p class="card-farsi" lang="fa">عشق باش</p>
    <div class="card-art card-art--gold" role="img" aria-label="Painting of red flowers on a golden ground"></div>
  </article>
  <article class="art-card card-be">
    <div class="card-art card-art--pencil" role="img" aria-label="Pencil drawing of a bird on a branch"></div>
    <p class="card-word">Be</p>
    <p class="card-word-farsi" lang="fa">بودن</p>
  </article>
  <article class="art-card card-joy">
    <h3 class="card-title">BE JOY</h3>
    <p class="card-farsi" lang="fa">شاد باش</p>
    <div class="card-art card-art--ivory" role="img" aria-label="Painting of orange dahlias"></div>
  </article>
  <article class="art-card card-still">
    <div class="card-art card-art--pencil" role="img" aria-label="Pencil drawing of a small bird"></div>
    <p class="card-word">Still</p>
    <p class="card-word-farsi" lang="fa">هنوز</p>
  </article>

  <h1 class="headline">FREE DAVOR</h1>
  <p class="band-pitch">Buy Davor’s Beautiful Art Cards<br><strong>Support Him</strong><br>Help Davor Pay For His Sponsorship<br>to Freedom</p>

  <blockquote class="quote"><span class="quote-mark">“</span>It’s true that my body is prisoner.... But my thoughts and my heart are not prisoner.. No one can imprison my thoughts and my heart. Because my thoughts and my heart are with those who I love them” - Davor Kelmandi.</blockquote>

  <p class="call-out">READ DAVOR’S STORY AND BUY HIS<br>BEAUTIFUL HAND DRAWN ART CARDS.<br>HELP SAVE A LIFE</p>

  <a class="url-ribbon" aria-label="www.davorsketch.net">
    <svg viewBox="0 0 248 31" preserveAspectRatio="none" aria-hidden="true">
      <polygon points="0,0 248,0 236,15.5 248,31 0,31 12,15.5" fill="#1d4d2c"/>
      <polygon points="5,3 243,3 233,15.5 243,28 5,28 15,15.5" fill="#f4e7c4"/>
    </svg>
    <span>www.<b>davorsketch</b>.net</span>
  </a>
</section>

<section class="postcard postcard--back" aria-label="Postcard back">
  <div class="wood" role="img" aria-label="Weathered brown wooden planks"></div>
  <div class="band"></div>

  <article class="art-card card-hope">
    <h3 class="card-title">BE HOPE</h3>
    <p class="card-farsi" lang="fa">امیدوار باش</p>
    <div class="card-art card-art--ivory" role="img" aria-label="Painting of orange lilies"></div>
  </article>
  <article class="art-card card-gentle">
    <div class="card-art card-art--pencil" role="img" aria-label="Pencil drawing of a cardinal on a branch"></div>
    <p class="card-word">Gentle</p>
    <p class="card-word-farsi" lang="fa">آرام</p>
  </article>
  <article class="art-card card-compassion">
    <h3 class="card-title">BE COMPASSION</h3>
    <p class="card-farsi" lang="fa">مهربان باش</p>
    <div class="card-art card-art--ivory" role="img" aria-label="Painting of red tulips"></div>
  </article>
  <article class="art-card card-framed">
    <div class="card-art card-art--rose" role="img" aria-label="Framed painting of an orange and black bird on a blossom branch with a hand written message"></div>
  </article>

  <div class="story">
    <p>Davor Kelmandi, a young Hazara man from Afghanistan, has been illegally held captive in an Indonesian Detention Centre for more than four years. He is a Refugee and prisoner without any crime. The Hazara are a ruthlessly persecuted people. Davor is alone in the world and bravely escaped his country to begin a new free life never expecting to be imprisoned and detained for 4 years.</p>
    <p>An artist and photographer, Davor refuses to allow his creative nature to be imprisoned. He draws each day ! He draws sunny flowers and delicate fragile birds which sing of his freedom. The only future for Davor is to be sponsored to a free country. It costs thousands. He is raising funds by selling his unique art. Davor’s daily drawings have become individual Greeting Cards and his beautiful cards are now for sale to fund his future. Buy Davor’s Greeting Cards to help him pay his way to freedom.</p>
  </div>

  <figure class="portrait">
    <div class="portrait-photo" role="img" aria-label="Photo of Davor, a young man in a white football shirt"></div>
  </figure>

  <p class="offer">Individual Cards. Sets of Cards. Stunning Framed Art Works.<br>Beautiful black line drawing cards and full colour cards available.<br>Davor’s Cards, Art and Designs are available from</p>

  <a class="url-ribbon" aria-label="www.davorsketch.net">
    <svg viewBox="0 0 260 34" preserveAspectRatio="none" aria-hidden="true">
      <polygon points="0,0 260,0 248,17 260,34 0,34 12,17" fill="#1d4d2c"/>
      <polygon points="5,3 255,3 245,17 255,31 5,31 15,17" fill="#f4e7c4"/>
    </svg>
    <span>www.<b>davorsketch</b>.net</span>
  </a>

  <p class="email">
    <svg width="12" height="9" viewBox="0 0 12 9" aria-hidden="true">
      <rect x="0.5" y="0.5" width="11" height="8" fill="none" stroke="#fff"/>
      <polyline points="0.5,0.5 6,5 11.5,0.5" fill="none" stroke="#fff"/>
    </svg>
    helpdavor2031@mailpost.net
  </p>
</section>

</body>
</html>
```